Health & Nutrition - Business Cards

Needs to look new-age, simple, and elegant. The cards are for my services/counsel in health and nutrition - which include mind, body, and soul. I would like to see something clean and simple but beautiful. Can have a plain background or with a pattern but I don't want it to take away from my contact details. Therefore, my info can be on the back of the card and a nice front design. I really like the flower of life symbol. The name of my business is called Willow Lantern.

Target Market(s)

Clients - men & women age 20-60. Adults, parents, teachers, sick individuals seeking nutrient counseling and dietary management.

Industry/Entity Type

Nutritionist

Contact Information for Business Card

Tomas Brindle
Cell: 345-582-7046
Email: tbrindle@mailvane.net

Colors
33a6d7
33b8a4
add136
ffffff
5c5c5c
f04a50
fbee3f
cedeed
85cae6

Requirements
Nice to have
• Maybe it can have some sort of sacred geometry as well, but not required. Nice to have the colors that I choose in the project but feel free to come up with your own use of colors. Thanks! =)

```html
<!DOCTYPE html>
<html lang="en">
<head>
<meta charset="utf-8">
<title>Willow Lantern – Business Cards</title>
<link href="https://fonts.googleapis.com/css2?family=Work+Sans:wght@400;500&display=swap" rel="stylesheet">
<style>
  :root {
    --stage: #e6e7e8;
    --card-light: #ffffff;
    --card-light-shade: #e9ecec;
    --card-dark: #47494a;
    --card-dark-shade: #5a5d5e;
    --brand-orange: #e0702a;
    --accent-green: #9ccb2e;
    --text-grey: #4a4a4a;
  }
  * { box-sizing: border-box; margin: 0; padding: 0; }
  html, body {
    width: 1200px; height: 900px; overflow: hidden;
    background: var(--stage);
    font-family: "Work Sans", Arial, sans-serif;
  }
  .sheet {
    width: 1200px; height: 900px;
    display: flex; flex-direction: column; align-items: center; justify-content: center;
    gap: 50px;
  }
  .card {
    position: relative;
    width: 630px; height: 360px;
    border-radius: 22px;
    overflow: hidden;
    box-shadow: 0 10px 30px rgba(0,0,0,0.18);
  }
  .card-texture { position: absolute; inset: 0; }
  .card--front .card-texture {
    background: radial-gradient(ellipse at 45% 40%, var(--card-light) 0%, var(--card-light) 30%, var(--card-light-shade) 100%);
  }
  .card--back .card-texture {
    background: radial-gradient(ellipse at 50% 50%, var(--card-dark-shade) 0%, var(--card-dark) 100%);
  }
  .brand-name {
    position: absolute;
    color: var(--brand-orange);
    font-weight: 500;
    letter-spacing: 0.08em;
    text-transform: uppercase;
    white-space: nowrap;
  }
  .card--front .brand-name { left: 40px; top: 108px; font-size: 25px; }
  .card--back .brand-name {
    left: 0; right: 0; top: 50%; transform: translateY(-50%);
    text-align: center; font-size: 40px;
  }
  .divider {
    position: absolute; left: 340px; top: 150px;
    width: 2px; height: 140px; background: var(--accent-green);
  }
  .contact { position: absolute; left: 362px; top: 156px; }
  .contact-name {
    color: var(--accent-green);
    font-size: 24px; font-weight: 500; letter-spacing: 0.05em;
    text-transform: uppercase; line-height: 1.1;
  }
  .contact-role { color: var(--text-grey); font-size: 14px; margin: 4px 0 12px; }
  .contact-list { list-style: none; }
  .contact-item {
    display: flex; align-items: center; gap: 9px;
    color: var(--text-grey); font-size: 15px; line-height: 1.6;
  }
  .contact-icon { width: 12px; height: 12px; flex: none; }
</style>
</head>
<body>
<main class="sheet">

  <section class="card card--front">
    <div class="card-texture" role="img" aria-label="Faint overlapping-circle sacred geometry pattern on white"></div>
    <div class="brand-name">Willow Lantern</div>
    <div class="divider"></div>
    <div class="contact">
      <div class="contact-name">Tomas Brindle</div>
      <div class="contact-role">Director</div>
      <ul class="contact-list">
        <li class="contact-item">
          <svg class="contact-icon" viewBox="0 0 12 12" aria-hidden="true"><path d="M3 1 L5 3.5 L4 5 Q5 7 7 8 L8.5 7 L11 9 L9.5 11 Q5 11 2.5 8 Q0.5 5 1 2.5 Z" fill="var(--accent-green)"/></svg>
          345-582-7046
        </li>
        <li class="contact-item">
          <svg class="contact-icon" viewBox="0 0 12 12" aria-hidden="true"><rect x="0.5" y="2.5" width="11" height="7.5" rx="1" fill="none" stroke="var(--accent-green)" stroke-width="1.3"/><path d="M1 3 L6 7 L11 3" fill="none" stroke="var(--accent-green)" stroke-width="1.3"/></svg>
          tbrindle@mailvane.net
        </li>
        <li class="contact-item">
          <svg class="contact-icon" viewBox="0 0 12 12" aria-hidden="true"><circle cx="6" cy="6" r="5.3" fill="none" stroke="var(--accent-green)" stroke-width="1.2"/><ellipse cx="6" cy="6" rx="2.3" ry="5.3" fill="none" stroke="var(--accent-green)" stroke-width="1"/><path d="M0.7 6 H11.3" stroke="var(--accent-green)" stroke-width="1"/></svg>
          www.willowlantern.net
        </li>
      </ul>
    </div>
  </section>

  <section class="card card--back">
    <div class="card-texture" role="img" aria-label="Subtle overlapping-circle sacred geometry pattern on charcoal"></div>
    <div class="brand-name">Willow Lantern</div>
  </section>

</main>
</body>
</html>
```